Poster for the 'LFA Monthly Draw'

We are a parents association for a senior school and have a number of money raising activities.

We require a poster a lucky draw where parents who subscribe £20 for the school year are entered into a monthly cash prize draw.

Draws are performed monthly. Some detail about it is available here

http://www.larchfield.example-school.uk/lfa/what-is-350-circle

We are changing the name from 'The 350 circle' to 'LFA Monthly draw', although we don't need the name change highlighted or noted on the poster

A logo is available on the word document application at the above link. Not sure of the quality. I can look to obtain a better resolution, but no promises.

A brief overview of the LFA can be read here for any thoughts / inspiration.

We don't want any reference to specific items purchased, unless we can easily update this on the poster ourselves.

http://www.larchfield.example-school.uk/lfa

Target Market(s)

Parents of school kids aged 13 to 17 from whom we are trying to raise contributions to so as to provide funding to school departments who have need to additional items that are not available via the school budget.

Industry/Entity Type

School

Requirements
Must have
• LFA Parents association logo, as in the current 350 circle application, should appear.
• Reference to the amount to be contributed of £20 for the year.
• Reference to the monthly prize draw amounts of
• 1st prize - £30
• 2nd prize - £20
• 3rd Prize £10
• Please note all spellings are to be UK english, not American english.
• Payment methods should be highlighted being
• - Trenvolo- via the school website
• - Cash
• - Cheque - Payable to Larchfield’s Parents’ Association 350 Circle
• No specific colour scheme, although you will see from the school website what the colours are and this should have some representation, but not overbearing.
• The following text is to appear
• The LFA Monthly Draw is a fundraiser for the Larchfield Parent Association. We raise funds to provide the best possible resources and facilities, for your children, to enhance their learning.
• Thank you for your support of the LFA
Nice to have
• The font type is not to critical, however, it should be easy to read in a short space of time as people are walking past, so not excessive amounts of text detail and not to small a font.

```html
<!DOCTYPE html>
<html lang="en-GB">
<head>
<meta charset="utf-8">
<title>The LFA Monthly Draw</title>
<link rel="stylesheet" href="https://fonts.googleapis.com/css2?family=Bodoni+Moda:wght@400;600;700&family=Arimo:wght@400&display=swap">
<style>
  :root {
    --wine-deep: #6b0f14;
    --wine: #7d1419;
    --wine-mid: #8e1f24;
    --scarlet: #b31f26;
    --band-grey: #cfcfcf;
    --paper: #ececec;
    --paper-light: #f6f6f6;
    --ink: #1c1c1c;
    --white: #ffffff;
    --backdrop: #e4e4e4;
    --serif: "Bodoni Moda", "Didot", Georgia, serif;
    --sans: "Arimo", Arial, sans-serif;
  }
  * { box-sizing: border-box; margin: 0; padding: 0; }
  html, body {
    width: 1200px;
    height: 1200px;
    overflow: hidden;
    background: var(--backdrop);
  }
  .poster {
    position: absolute;
    left: 200px;
    top: 35px;
    width: 800px;
    height: 1130px;
    background: var(--paper);
    display: flex;
    flex-direction: column;
    box-shadow: 0 6px 24px rgba(0,0,0,0.12);
  }
  .masthead {
    display: flex;
    height: 215px;
  }
  .brand {
    width: 190px;
    background: var(--paper-light);
    display: flex;
    flex-direction: column;
    align-items: center;
    justify-content: center;
    gap: 10px;
    padding: 16px;
  }
  .brand-mark {
    width: 62px;
    height: 62px;
    border-radius: 50%;
    background: var(--wine);
  }
  .brand-name {
    font-family: var(--serif);
    font-weight: 600;
    font-size: 15px;
    line-height: 1.2;
    color: var(--wine);
    text-align: center;
  }
  .title-band {
    flex: 1;
    background: linear-gradient(135deg, var(--wine) 0%, var(--wine-deep) 100%);
    display: flex;
    align-items: center;
    padding-left: 74px;
  }
  .title {
    font-family: var(--serif);
    font-weight: 400;
    font-size: 62px;
    line-height: 1.12;
    color: var(--paper-light);
  }
  .intro {
    background: var(--band-grey);
    padding: 26px 32px;
    font-family: var(--serif);
    font-weight: 700;
    font-size: 24px;
    line-height: 1.5;
    color: var(--ink);
  }
  .prizes {
    flex: 1;
    background: linear-gradient(180deg, var(--paper-light) 0%, var(--paper) 100%);
    padding: 30px 0 0 210px;
  }
  .prizes-heading {
    font-family: var(--serif);
    font-weight: 600;
    font-size: 74px;
    line-height: 1;
    color: var(--wine);
    margin-bottom: 8px;
  }
  .prize-list { list-style: none; }
  .prize {
    width: 470px;
    height: 92px;
    margin-bottom: 30px;
    display: flex;
    align-items: center;
    padding-left: 70px;
    font-family: var(--serif);
    font-size: 54px;
    color: var(--paper-light);
  }
  .prize sup { font-size: 30px; vertical-align: 22px; }
  .prize-first { background: var(--wine-deep); }
  .prize-second { background: var(--wine-mid); }
  .prize-third { background: var(--scarlet); }
  .payment {
    background: var(--band-grey);
    padding: 26px 50px 24px;
    font-family: var(--sans);
    color: var(--ink);
  }
  .payment-heading { font-size: 19px; margin-bottom: 14px; }
  .payment-list { list-style: none; font-size: 21px; line-height: 1.5; }
  .payment-list li::before { content: "\2022\00a0"; }
  .closing {
    background: linear-gradient(135deg, var(--wine) 0%, var(--wine-deep) 100%);
    padding: 26px 50px 30px;
    font-family: var(--serif);
    font-size: 21px;
    line-height: 1.45;
    color: var(--paper-light);
  }
  .closing p + p { margin-top: 14px; }
</style>
</head>
<body>
  <main class="poster">
    <header class="masthead">
      <div class="brand">
        <span class="brand-mark"></span>
        <span class="brand-name">Larchfield School Parents Association</span>
      </div>
      <div class="title-band">
        <h1 class="title">The LFA<br>Monthly&nbsp; Draw</h1>
      </div>
    </header>

    <p class="intro">Parents who subscribe £20 for the school year are entered into a monthly cash prize draw.</p>

    <section class="prizes">
      <h2 class="prizes-heading">Prizes:</h2>
      <ul class="prize-list">
        <li class="prize prize-first">1<sup>st</sup>&nbsp;-&nbsp;£30</li>
        <li class="prize prize-second">2<sup>nd</sup>&nbsp;-&nbsp;£20</li>
        <li class="prize prize-third">3<sup>rd</sup>&nbsp;-&nbsp;£10</li>
      </ul>
    </section>

    <section class="payment">
      <h3 class="payment-heading">Payment methods :</h3>
      <ul class="payment-list">
        <li>Trenvolo- via the school website</li>
        <li>Cash</li>
        <li>Cheque - Payable to Larchfield’s Parents’ Association 350 Circle</li>
      </ul>
    </section>

    <footer class="closing">
      <p>The LFA Monthly Draw is a fundraiser for the Larchfield Parent Association. We raise funds to provide the best possible resources and facilities, for your children, to enhance their learning.</p>
      <p>Thank you for your support of the LFA</p>
    </footer>
  </main>
</body>
</html>
```